Orva Business Card

we need a business card for flooring business called Orva Flooring, the design should be black and white. we have 2 locations

Ellsworth Showroom
527 Kellerman Road,
Ellsworth VIC 3136

Carrow Showroom
462 Bramwell Hwy,
Carrow VIC 3207

email : sales@orvaflooring.com.au
(03) 9471 2830

Please inform we sell , Laminate, Hybrid, Timber, carpet and commercial flooring

```html
<!DOCTYPE html>
<html lang="en">
<head>
<meta charset="utf-8">
<title>Orva Flooring Business Card</title>
<link href="https://fonts.googleapis.com/css2?family=Montserrat:wght@300;400;500;700&display=swap" rel="stylesheet">
<style>
  :root {
    --ink: #111111;
    --paper: #ffffff;
    --stage: #d9d9d9;
    --muted: #333333;
    --ghost: #f1f1f1;
  }
  * { box-sizing: border-box; margin: 0; padding: 0; }
  html, body {
    width: 1200px; height: 1200px; overflow: hidden;
    background: var(--stage);
    font-family: "Montserrat", sans-serif;
  }
  .card {
    position: absolute; left: 160px;
    width: 880px; height: 500px;
    border-radius: 28px; overflow: hidden;
  }
  /* Brand side */
  .card--brand { top: 70px; background: var(--ink); color: var(--paper); }
  .brand-name {
    position: absolute; top: 90px; width: 100%; text-align: center;
    font-weight: 400; font-size: 110px; letter-spacing: 14px; line-height: 1;
  }
  .brand-sub {
    position: absolute; top: 215px; width: 100%; text-align: center;
    font-weight: 400; font-size: 44px; letter-spacing: 4px;
  }
  .we-sell {
    position: absolute; top: 298px; left: 50%; transform: translateX(-50%);
    font-weight: 700; font-size: 22px; padding: 0 20px 12px;
    border-bottom: 2px solid var(--paper);
  }
  .services {
    position: absolute; bottom: 56px; width: 100%; text-align: center;
    font-weight: 400; font-size: 24px; letter-spacing: 1px;
  }
  /* Contact side */
  .card--contact { top: 630px; background: var(--paper); color: var(--ink); }
  .ghost-name {
    position: absolute; left: 420px; top: 300px;
    font-weight: 400; font-size: 130px; letter-spacing: 6px;
    color: var(--ghost); line-height: 1; white-space: nowrap;
  }
  .headline {
    position: absolute; left: 40px; top: 22px;
    font-weight: 400; font-size: 142px; letter-spacing: 2px; line-height: 1;
  }
  .person { position: absolute; left: 60px; top: 330px; }
  .person-name { font-weight: 700; font-size: 34px; }
  .person-role { font-weight: 400; font-size: 21px; margin-top: 4px; padding-left: 56px; }
  .divider {
    position: absolute; left: 400px; top: 200px;
    width: 2px; height: 260px; background: var(--ink);
  }
  .details {
    position: absolute; left: 430px; top: 196px;
    font-size: 19px; line-height: 1.3; color: var(--muted);
  }
  .showroom { margin-bottom: 14px; }
  .showroom-title { font-weight: 700; color: var(--ink); }
  .contact-list { list-style: none; margin-top: 6px; }
  .contact-list li { display: flex; align-items: center; gap: 10px; margin-bottom: 4px; }
  .contact-list svg { width: 18px; height: 18px; fill: var(--ink); flex: none; }
</style>
</head>
<body>
  <section class="card card--brand">
    <div class="brand-name">ORVA</div>
    <div class="brand-sub">FLOORING</div>
    <div class="we-sell">We Sell</div>
    <div class="services">• Laminate • Hybrid • Timber • carpet and commercial flooring</div>
  </section>

  <section class="card card--contact">
    <div class="ghost-name" aria-hidden="true">ORVA</div>
    <div class="headline">FLOORING</div>

    <div class="person">
      <div class="person-name">Lena Marsh</div>
      <div class="person-role">Managing Director</div>
    </div>

    <div class="divider"></div>

    <div class="details">
      <div class="showroom">
        <div class="showroom-title">Carrow Showroom</div>
        <div>462 Bramwell Hwy,</div>
        <div>Carrow VIC 3207</div>
      </div>
      <div class="showroom">
        <div class="showroom-title">Ellsworth Showroom</div>
        <div>527 Kellerman Road,</div>
        <div>Ellsworth VIC 3136</div>
      </div>
      <ul class="contact-list">
        <li>
          <svg viewBox="0 0 24 24"><path d="M6.6 10.8a15 15 0 0 0 6.6 6.6l2.2-2.2c.3-.3.7-.4 1-.2 1.1.4 2.3.6 3.6.6.6 0 1 .4 1 1V20c0 .6-.4 1-1 1A17 17 0 0 1 3 4c0-.6.4-1 1-1h3.5c.6 0 1 .4 1 1 0 1.3.2 2.5.6 3.6.1.3 0 .7-.2 1z"/></svg>
          <span>(03) 9471 2830</span>
        </li>
        <li>
          <svg viewBox="0 0 24 24"><path d="M2 5h20v14H2z M2 5l10 8 10-8" stroke="#fff" stroke-width="1.5"/></svg>
          <span>sales@orvaflooring.com.au</span>
        </li>
        <li>
          <svg viewBox="0 0 24 24"><circle cx="12" cy="12" r="10"/><path d="M2 12h20M12 2c3 3 3 17 0 20M12 2c-3 3-3 17 0 20" stroke="#fff" stroke-width="1.3" fill="none"/></svg>
          <span>www.orvaflooring.com.au</span>
        </li>
      </ul>
    </div>
  </section>
</body>
</html>
```